Velmora, Inc. Website

Looking for a website design and build for Velmora, Inc. an intellectual property incubator for the recreational and medical cannabis space in California. Our logo and brand identity has been completed website so w can begin our SEO leg of brand development.

See more details in Must haves and Nice to Haves

Target Market(s)

Target market

Vision

Our proprietary ideas have been developed to shift the approach on how whole body wellness and healing is achieved. Velmora's patent pending designs and formulations are rooted in the desire to find the most efficient, customizable, and convenient  method to precisely micro-despense whole plant cannabis extracts. 

Our ideas, designs and development team are supported by leading chemists specializing in cannabis extraction technology, leading medical doctors collaborating to develop our proprietary cannabis formulations and a passion to shift landscape of healing from a dependency on isolated symptom treatment to whole body, whole plant, whole life wellness for ourselves and our families. 

Goal

Develop, patent, and trademark our proprietary devices, formulations, and ideas for the purpose of licensing, manufacturing and distributing in the Cannabis Industry.

Industry/Entity Type

Medical

Coding

Coded - Design and coding required

Number of Pages Required

5+ page

Font styles to use
Other font styles liked:
• See Brand Identity Guide

Requirements
Must have
• Look and Feel: We are developing products, intellectual property and platforms to bring together the medical, health & wellness, and cannabis industries to provide individuals and families alike a innovative solutions to chronic illness, mood disorders, and over all wellbeing.
• Page Titles
• Home - Landing Page
• Vision-
• IP Technology & Products - will remain under construction
• Team
• Strategic Partners – will remain under construction
• Invest- will need a form to aquire contact information as well as have some questions that need to be answered to help evaluate to the potential interested party
• Contact Us– Velmora address and info@ email
Nice to have
• Images - wellness, balance, health, healing, herbs, not just cannabis, aromatherapy, mediation, energy work, dna, scientific research, microdosing, medical testing
• Style sleek and innovative - cutting edge technology - inspire to learn more
• For Colors and Fonts - See Brand Identity Guide
• Site layouts that we like are:
• http://www.example-tarnwick.com
• https://www.example-plovisandcare.com
• https://www.example-durnique.com
• https://www.example-zobra.com
• https://www.example-quessa.com
Should not have
• Should not have to many cannabis images - imagery should balanced between cannabis, medical & recreational, health and wellness, mental health

```html
<!DOCTYPE html>
<html lang="en">
<head>
<meta charset="utf-8">
<title>Velmora, Inc</title>
<link rel="stylesheet" href="https://fonts.googleapis.com/css2?family=Lato:wght@300&family=Merriweather:ital,wght@1,400&family=Poppins:wght@300;400;500&display=swap">
<style>
  :root {
    --sky-top: #0b3566;
    --sky-mid: #2c5a8c;
    --sky-low: #5b7fa6;
    --grass: #3d8a2a;
    --grass-deep: #2c6a1d;
    --family-warm: rgba(196, 168, 136, 0.6);
    --family-mid: rgba(150, 132, 112, 0.35);
    --white: #ffffff;
    --nav-green: #5ed23a;
    --purple: #7a3aa6;
    --arrow-line: rgba(255,255,255,0.75);
  }
  * { box-sizing: border-box; margin: 0; padding: 0; }
  html, body { width: 1200px; height: 605px; overflow: hidden; }
  body { position: relative; font-family: "Poppins", sans-serif; color: var(--white); background: var(--sky-top); }

  .hero-backdrop {
    position: absolute; inset: 0;
    background: linear-gradient(180deg, var(--sky-top) 0%, var(--sky-mid) 45%, var(--sky-low) 78%, var(--grass) 81%, var(--grass-deep) 100%);
  }
  .hero-family {
    position: absolute; left: 600px; top: 32px; width: 470px; height: 500px;
    border-radius: 48% 48% 30% 30%;
    background: radial-gradient(ellipse 50% 55% at 55% 50%, var(--family-warm) 0%, var(--family-mid) 55%, transparent 80%);
  }

  .brand {
    position: absolute; left: 51px; top: 5px;
    display: flex; align-items: center; gap: 10px;
  }
  .brand-mark {
    width: 52px; height: 52px; border-radius: 50%;
    border: 2px solid var(--white);
  }
  .brand-name {
    font-family: "Lato", sans-serif; font-weight: 300; font-size: 27px; color: var(--white);
  }

  .main-nav {
    position: absolute; top: 25px; right: 64px;
    display: flex; gap: 26px;
    font-size: 9px; color: var(--nav-green);
  }

  .hero-copy { position: absolute; left: 109px; top: 222px; }
  .hero-kicker {
    font-family: "Merriweather", serif; font-style: italic; font-size: 28px; font-weight: 400; line-height: 1.4;
  }
  .hero-title {
    margin-top: 8px;
    font-family: "Poppins", sans-serif; font-weight: 300; font-size: 42px; letter-spacing: 0.3px; line-height: 1.15;
  }
  .hero-actions { position: absolute; left: 115px; top: 345px; display: flex; gap: 16px; }
  .btn {
    height: 31px; display: flex; align-items: center; justify-content: center;
    font-size: 10px; font-weight: 500; color: var(--white);
  }
  .btn-primary { width: 114px; background: var(--purple); }
  .btn-outline { width: 150px; border: 1.5px solid var(--white); }

  .slide-arrow { position: absolute; top: 289px; width: 44px; height: 44px; }
  .slide-arrow-prev { left: 25px; }
  .slide-arrow-next { left: 1130px; }
</style>
</head>
<body>
  <div class="hero-backdrop"></div>
  <div class="hero-family" role="img" aria-label="Mother and father walking hand in hand with their toddler across green grass under a clear blue sky"></div>

  <header>
    <div class="brand">
      <span class="brand-mark"></span>
      <span class="brand-name">Velmora, Inc</span>
    </div>
    <nav class="main-nav">
      <span>Vision</span>
      <span>IP Technology &amp; Products</span>
      <span>Invest</span>
      <span>Strategic Partners</span>
      <span>Team</span>
      <span>News</span>
      <span>Contact Us</span>
    </nav>
  </header>

  <section class="hero-copy">
    <p class="hero-kicker">Join us on a journey towards</p>
    <h1 class="hero-title">A new era in healthcare</h1>
  </section>
  <div class="hero-actions">
    <span class="btn btn-primary">Our Vision</span>
    <span class="btn btn-outline">Join the program</span>
  </div>

  <svg class="slide-arrow slide-arrow-prev" viewBox="0 0 44 44" aria-label="Previous slide">
    <circle cx="22" cy="22" r="21" fill="none" stroke="var(--arrow-line)" stroke-width="1"/>
    <path d="M32 22H12M19 15l-7 7 7 7" fill="none" stroke="var(--arrow-line)" stroke-width="1.2"/>
  </svg>
  <svg class="slide-arrow slide-arrow-next" viewBox="0 0 44 44" aria-label="Next slide">
    <circle cx="22" cy="22" r="21" fill="none" stroke="var(--arrow-line)" stroke-width="1"/>
    <path d="M12 22H32M25 15l7 7-7 7" fill="none" stroke="var(--arrow-line)" stroke-width="1.2"/>
  </svg>
</body>
</html>
```